SOL Book cover redo

I wrote a book called Shadows Over the Lantern over ten years ago. I have revised and update the book and need a new cover. It should reflect the original idea and correlate with volumes two and three that came out later. So it doesn't need to be completely different...but enough to make it easy to see that it is a new version.
My title needs to be updated as well as it should say Shadows Over the Lantern 1 (to flow with volumes 2 and 3).

```html
<!DOCTYPE html>
<html lang="en">
<head>
<meta charset="utf-8">
<title>Shadows Over the Lantern 1 — Book Cover</title>
<link rel="stylesheet" href="https://fonts.googleapis.com/css2?family=Black+Ops+One&family=Oswald:wght@700&family=Saira+Condensed:wght@600&family=Saira:ital,wght@1,700&display=swap">
<style>
  :root {
    --ink-black: #000000;
    --sky-blue: #5cc3ec;
    --paper-white: #ffffff;
    --fire-deep: #c7321a;
    --fire-mid: #f07a1e;
    --fire-light: #ffc83a;
    --helix-orange: #e8672c;
    --plasma-blue: #2f74d8;
    --plasma-night: #070d2a;
  }
  * { margin: 0; padding: 0; box-sizing: border-box; }
  html, body { width: 841px; height: 1200px; overflow: hidden; background: var(--ink-black); }
  .cover {
    position: relative;
    width: 841px;
    height: 1200px;
    background: var(--ink-black);
    overflow: hidden;
  }
  .cover__blurb {
    position: absolute;
    top: 50px;
    left: 0;
    width: 100%;
    text-align: center;
    font-family: "Saira", sans-serif;
    font-style: italic;
    font-weight: 700;
    font-size: 44px;
    letter-spacing: 1px;
    color: var(--sky-blue);
  }
  .cover__title {
    position: absolute;
    top: 0;
    left: 0;
    width: 841px;
    height: 560px;
  }
  .cover__title .title-line {
    font-family: "Black Ops One", sans-serif;
    fill: var(--sky-blue);
  }
  .cover__title .title-subtitle {
    font-family: "Saira Condensed", sans-serif;
    font-weight: 600;
    fill: var(--sky-blue);
  }
  .cover__artwork {
    position: absolute;
    top: 566px;
    left: 0;
    width: 841px;
    height: 460px;
    background:
      radial-gradient(ellipse 55% 30% at 60% 55%, rgba(232,103,44,0.85), rgba(232,103,44,0) 70%),
      radial-gradient(ellipse 70% 40% at 45% 60%, rgba(110,190,255,0.8), rgba(47,116,216,0.4) 55%, rgba(7,13,42,0) 85%),
      linear-gradient(to bottom, var(--ink-black) 0%, var(--plasma-night) 20%, var(--plasma-night) 80%, var(--ink-black) 100%);
  }
  .cover__author {
    position: absolute;
    top: 1046px;
    left: 0;
    width: 100%;
    text-align: center;
    font-family: "Oswald", sans-serif;
    font-weight: 700;
    font-size: 52px;
    letter-spacing: 1px;
    color: var(--paper-white);
  }
  .cover__foreword {
    position: absolute;
    top: 1128px;
    left: 0;
    width: 100%;
    text-align: center;
    font-family: "Saira Condensed", sans-serif;
    font-weight: 600;
    font-size: 31px;
    letter-spacing: 7px;
    color: var(--sky-blue);
  }
</style>
</head>
<body>
<main class="cover">
  <p class="cover__blurb">"A thrilling read!"</p>

  <svg class="cover__title" viewBox="0 0 841 560" aria-label="Shadows Over the Lantern 1: Watchers, Visitors and the Last Deceiver">
    <defs>
      <linearGradient id="fire-fill" x1="0" y1="0" x2="0" y2="1">
        <stop offset="0" stop-color="#ffc83a"/>
        <stop offset="0.5" stop-color="#f07a1e"/>
        <stop offset="1" stop-color="#c7321a"/>
      </linearGradient>
    </defs>
    <text class="title-line" x="96" y="284" font-size="168" textLength="640" lengthAdjust="spacingAndGlyphs">Shadows Over</text>
    <text class="title-line" x="86" y="408" font-size="92" textLength="138" lengthAdjust="spacingAndGlyphs">the</text>
    <text class="title-line" x="244" y="476" font-size="190" textLength="418" lengthAdjust="spacingAndGlyphs">LANTERN</text>
    <text class="title-line" x="676" y="532" font-size="170" style="fill:url(#fire-fill)" textLength="32" lengthAdjust="spacingAndGlyphs">1</text>
    <text class="title-subtitle" x="239" y="530" font-size="23" textLength="428" lengthAdjust="spacing">Watchers, Visitors and the Last Deceiver</text>
  </svg>

  <div class="cover__artwork" role="img" aria-label="Orange DNA double helix twisting across glowing blue plasma on a dark starry field"></div>

  <p class="cover__author">Dr Daniel Harrow</p>
  <p class="cover__foreword">Foreword by Tim Hollis</p>
</main>
</body>
</html>
```